Business card design needed

I have a small café in a small coastal town on the Central coast of NSW (Aus) I need something simple but noticeable. My café is on the main rd and while there is a lot of passing traffic I need a logo which will make people notice us, either through pamphlets or signage. We make almost everything freshly on the premises including cakes, burgers, hot chips, coffees and milkshakes. we also sell some cake decorating supplies. I am pretty open to designs and don't mind if these items are incorporated in the design. My frontage is aqua and my outdoor furniture is beige. Inside we have a small amount of aqua and the walls are white. I am happy for any variations of these colours or anything which goes with the aqua.

Contact Information for Business Card

Mug & Muffin Café
418 Ridge St West Darbin
02 48 61 2795
Open for breakfast and lunch
from 6am Monday - Saturday

```html
<!DOCTYPE html>
<html lang="en">
<head>
<meta charset="utf-8">
<title>Mug &amp; Muffin Café — Business Card</title>
<link rel="stylesheet" href="https://fonts.googleapis.com/css2?family=Alegreya:wght@400;700&display=swap">
<style>
  :root {
    --page: #ecebe8;
    --peach: #fcdcbf;
    --aqua: #6db3a3;
    --aqua-text: #7cbcab;
    --peach-text: #f6d7bb;
    --cake-cream: #f4ecd8;
    --cake-brown: #a68f7a;
    --card-shadow: rgba(60, 50, 40, 0.18);
  }
  * { margin: 0; padding: 0; box-sizing: border-box; }
  html, body {
    width: 1200px;
    height: 900px;
    overflow: hidden;
    background: var(--page);
  }
  .canvas {
    position: relative;
    width: 1200px;
    height: 900px;
    font-family: "Alegreya", Georgia, serif;
  }
  .card {
    position: absolute;
    width: 520px;
    height: 316px;
    border-radius: 22px;
    box-shadow: 0 6px 18px var(--card-shadow);
  }
  .card-back {
    left: 70px;
    top: 150px;
    background: var(--peach);
  }
  .card-front {
    left: 610px;
    top: 434px;
    background: var(--aqua);
  }
  .cupcake-mark {
    position: absolute;
    width: 110px;
    height: 110px;
    border-radius: 6px;
    background: linear-gradient(to bottom, var(--cake-cream) 0 42%, var(--cake-brown) 42% 100%);
  }
  .card-back .cupcake-mark { left: 92px; top: 103px; }
  .card-front .cupcake-mark { left: 205px; top: 48px; }
  .contact-lines {
    position: absolute;
    left: 228px;
    top: 118px;
    color: var(--aqua-text);
    font-size: 19px;
    line-height: 1.25;
  }
  .cafe-name {
    position: absolute;
    left: 0;
    right: 0;
    top: 182px;
    text-align: center;
    color: var(--peach-text);
    font-size: 34px;
    font-weight: 700;
    letter-spacing: 0.5px;
  }
  .cafe-address {
    position: absolute;
    left: 0;
    right: 0;
    top: 236px;
    text-align: center;
    color: var(--peach-text);
    font-size: 21px;
    letter-spacing: 0.5px;
  }
</style>
</head>
<body>
<main class="canvas">
  <section class="card card-back">
    <div class="cupcake-mark" role="img" aria-label="Illustration of a cupcake with swirled cream icing in a striped paper case"></div>
    <p class="contact-lines">
      02 48 61 2795<br>
      Open for breakfast and lunch<br>
      from 6am Monday - Saturday
    </p>
  </section>
  <section class="card card-front">
    <div class="cupcake-mark" role="img" aria-label="Illustration of a cupcake with swirled cream icing in a striped paper case"></div>
    <h1 class="cafe-name">Mug &amp; Muffin Café</h1>
    <p class="cafe-address">418 Ridge St West Darbin</p>
  </section>
</main>
</body>
</html>
```